Financial Services Consultant needs a business card

We need a business card for a new consulting company based in Melbourne called
"Qorvel Insights". Tagline is Track, Review, Grow
We would like to see business card designs that are in line with the minimal style of the website www.qorvel-insights.example
The font I have used on the website is Proxima Nova and would like the same or similar font used on the business card with a minimal design in line with the website Two sided with "QORVEL INSIGHTS" TRACK, REVIEW, GROW on one side and name, title and contact details on the otther
Updates

Hi All, thanks for your submissions, much appreciated.

I have recently added some colour to my webiste, it is hex #3a7b74 for those that wish to use it
Thanks

Hi all

thanks very much for your design submissions I am very impressed and they are much appreciated.

Interms of general feedback please find below;

Colour: I am trying to stick to a minimal design and colour scheme for my website which is still under construction, up to 3 colours( www.qorvel-insights.example) it is currently black and white with a small amount of blue/green but I am open to suggestion/interpretations for a consulting company.

Card: I dont mind if it has rounded edges or straight, I was thinking about using a letterpress card if possible

Detail: the detail on the card will include; Name, Title, Mobile, Personal Email, Business Email,Web,Business Address

Once again thanks for submissions

Industry/Entity Type

Business

```html
<!DOCTYPE html>
<html lang="en">
<head>
<meta charset="utf-8">
<title>Qorvel Insights – Business Card</title>
<link rel="stylesheet" href="https://fonts.googleapis.com/css2?family=Montserrat:wght@600;700&family=Source+Sans+3:wght@400;600;700&display=swap">
<style>
  :root {
    --backdrop: #ecebe8;
    --card: #ffffff;
    --ink: #1a1a1a;
    --ink-soft: #3a3a3a;
    --ghost: #e2e2e2;
    --frame: #cfcfcf;
    --frame-faint: #ececec;
    --accent: #3a7b74;
    --card-shadow: rgba(0, 0, 0, 0.12);
  }
  * { box-sizing: border-box; margin: 0; padding: 0; }
  html, body {
    width: 1200px;
    height: 720px;
    overflow: hidden;
    background: var(--backdrop);
  }
  .canvas {
    width: 1200px;
    height: 720px;
    display: flex;
    align-items: center;
    justify-content: center;
    gap: 48px;
  }
  .card {
    position: relative;
    width: 540px;
    height: 309px;
    background: var(--card);
    box-shadow: 0 6px 18px var(--card-shadow);
    font-family: "Source Sans 3", Arial, sans-serif;
    color: var(--ink);
  }

  /* Contact side */
  .card--contact { text-align: center; }
  .ghost-frame {
    position: absolute;
    top: 40px;
    left: 50%;
    transform: translateX(-50%);
    padding: 2px 10px;
    border: 1px solid var(--frame-faint);
    white-space: nowrap;
  }
  .ghost-name {
    font-family: "Montserrat", Arial, sans-serif;
    font-weight: 600;
    font-size: 31px;
    letter-spacing: 4px;
    color: var(--ghost);
  }
  .person {
    position: absolute;
    top: 104px;
    left: 0;
    right: 0;
    font-size: 19px;
    font-weight: 700;
    color: var(--ink-soft);
  }
  .person .title {
    font-size: 14px;
    font-weight: 400;
    color: var(--accent);
  }
  .details {
    position: absolute;
    top: 142px;
    left: 0;
    right: 0;
    font-size: 14px;
    line-height: 24px;
    color: var(--ink-soft);
  }
  .details .row { display: flex; justify-content: center; align-items: center; gap: 6px; }
  .details .gap { width: 8px; }
  .icon { width: 12px; height: 12px; }
  .card--contact .tagline {
    position: absolute;
    top: 222px;
    left: 0;
    right: 0;
    font-size: 17px;
    color: var(--ink-soft);
  }

  /* Brand side */
  .brand-frame {
    position: absolute;
    top: 82px;
    left: 50%;
    transform: translateX(-50%);
    padding: 4px 12px 4px;
    border: 1px solid var(--frame);
    white-space: nowrap;
  }
  .brand-name {
    font-family: "Montserrat", Arial, sans-serif;
    font-weight: 700;
    font-size: 30px;
    letter-spacing: 4px;
    line-height: 40px;
    color: var(--ink);
  }
  .card--brand .tagline {
    text-align: right;
    padding-right: 40px;
    font-size: 16px;
    line-height: 22px;
    color: var(--ink-soft);
  }
  .card--brand .web-address {
    position: absolute;
    bottom: 46px;
    left: 0;
    right: 0;
    text-align: center;
    font-size: 16px;
    letter-spacing: 3px;
    color: var(--ink-soft);
  }
  .web-address strong { font-weight: 600; color: var(--ink); }
</style>
</head>
<body>
<main class="canvas">
  <section class="card card--contact" aria-label="Business card, contact side">
    <div class="ghost-frame"><div class="ghost-name">QORVEL INSIGHTS</div></div>
    <p class="person">Your Name, <span class="title">Title</span></p>
    <div class="details">
      <p class="row">Street Name, City Name, State Zip Code</p>
      <p class="row">
        <svg class="icon" viewBox="0 0 12 12" aria-hidden="true">
          <path d="M3 1 L5 3.2 L3.8 4.6 Q5 7.2 7.4 8.2 L8.8 7 L11 9 L9.6 11 Q3.6 10.6 1 3 Z" fill="var(--ink-soft)"/>
        </svg>
        <span>123-456-0789</span>
        <span class="gap"></span>
        <svg class="icon" viewBox="0 0 12 12" aria-hidden="true">
          <circle cx="6" cy="6" r="5" fill="none" stroke="var(--ink-soft)" stroke-width="1.2"/>
          <ellipse cx="6" cy="6" rx="2.2" ry="5" fill="none" stroke="var(--ink-soft)" stroke-width="1"/>
          <line x1="1" y1="6" x2="11" y2="6" stroke="var(--ink-soft)" stroke-width="1"/>
        </svg>
        <span>www.qorvel-insights.example</span>
      </p>
    </div>
    <p class="tagline">Track, Review, Grow</p>
  </section>

  <section class="card card--brand" aria-label="Business card, brand side">
    <div class="brand-frame">
      <h1 class="brand-name">QORVEL INSIGHTS</h1>
      <p class="tagline">Track, Review, Grow</p>
    </div>
    <p class="web-address">www.<strong>qorvel-insights</strong>.example</p>
  </section>
</main>
</body>
</html>
```